PTA Business Card

Seeking design for a business card, standard size. It is going to be for myself in regards to PTA - details:

Hollis Brantley Elementary School
PTA President
Peter Lund
563-555-0147
Lundy1984@mailbarn.example

Requirement:
Facebook icon? "Hollis Brantley PTA Rusk"
Twitter thing? I am new to twitter so not sure what to put, here is the link:
https://chirpline.example/HBRoversPTA

I was thinking on the front would be a notebook paper background? Not a requirement but was thinking it would look cool?

Total freedom here, let your creativity spread because I don't have any suggestions for design, sorry. Colors of school district are black and yellow.

Backside I am not sure exactly what to put on it.

```html
<!DOCTYPE html>
<html lang="en">
<head>
<meta charset="utf-8">
<title>PTA Business Card – Hollis Brantley Elementary School</title>
<link rel="stylesheet" href="https://fonts.googleapis.com/css2?family=Roboto+Slab:wght@300;700&display=swap">
<style>
  :root {
    --stage: #0a5f7a;
    --school-yellow: #fff500;
    --card-white: #ffffff;
    --ink: #141414;
    --marker-page: #2f4f8a;
    --marker-feed: #1a8fd8;
  }
  * { margin: 0; padding: 0; box-sizing: border-box; }
  html, body {
    width: 1200px;
    height: 1000px;
    overflow: hidden;
  }
  body {
    position: relative;
    background: var(--stage);
    font-family: "Roboto Slab", Rockwell, Georgia, serif;
    color: var(--ink);
  }
  .card {
    position: absolute;
    left: 263px;
    width: 618px;
    height: 363px;
    border-radius: 16px;
    overflow: hidden;
  }
  .card--front {
    top: 118px;
    background: var(--school-yellow);
    display: flex;
    align-items: center;
    justify-content: center;
    padding-bottom: 4px;
  }
  .card--back {
    top: 515px;
    background: var(--card-white);
  }
  .school-name {
    font-size: 28px;
    font-weight: 300;
    white-space: nowrap;
    letter-spacing: 0.2px;
  }
  .school-name strong { font-weight: 700; }
  .back-band {
    height: 133px;
    background: var(--school-yellow);
    display: flex;
    align-items: center;
    justify-content: center;
  }
  .contact-list {
    list-style: none;
    padding: 46px 0 0 35px;
    font-size: 18px;
    font-weight: 300;
    line-height: 25.5px;
  }
  .contact-list li {
    display: flex;
    align-items: center;
    white-space: nowrap;
  }
  .social-marker {
    width: 20px;
    height: 20px;
    margin-right: 7px;
    border-radius: 2px;
    flex: none;
  }
  .social-marker--page { background: var(--marker-page); }
  .social-marker--feed { background: var(--marker-feed); }
</style>
</head>
<body>
  <section class="card card--front" aria-label="Card front">
    <h1 class="school-name"><strong>Hollis Brantley</strong> Elementary School</h1>
  </section>

  <section class="card card--back" aria-label="Card back">
    <header class="back-band">
      <h2 class="school-name"><strong>Hollis Brantley</strong> Elementary School</h2>
    </header>
    <ul class="contact-list">
      <li class="contact-role">PTA President</li>
      <li class="contact-name">Peter Lund</li>
      <li class="contact-phone">563-555-0147</li>
      <li class="contact-email">lundy1984@mailbarn.example</li>
      <li class="contact-social"><span class="social-marker social-marker--page"></span>Hollis Brantley PTA Rusk</li>
      <li class="contact-social"><span class="social-marker social-marker--feed"></span>https://chirpline.example/HBRoversPTA</li>
    </ul>
  </section>
</body>
</html>
```